Flyer Design Project

BrookVale is an IT support company based in the UKl . We protect small busineses from online criminals, malware threats, and technology failure. We do this by creating layers of protection around our clients and their business. We show them the dangers they’re exposed to and how we’ll eliminate them.

We would like to market some special promotions for our managed it services. We want a double sided leaflet , One side will focus on sign up today and get 2 months free it support. On the other we would want to talk about we will not be beaten on price, we offer pro active IT support. Content would need to be along those lines.

I have added a brochure that we have used in the past. Use for ideas.

Industry/Entity Type

Business

```html
<!DOCTYPE html>
<html lang="en">
<head>
<meta charset="utf-8">
<title>BrookVale – Sign up today and get 2 months free IT support</title>
<link rel="stylesheet" href="https://fonts.googleapis.com/css2?family=Open+Sans:ital,wght@0,700;1,400;1,600;1,700&family=Roboto+Condensed:ital,wght@0,700;1,700&display=swap">
<style>
  :root {
    --sky: #1a9ad6;
    --sky-deep: #0a5fb0;
    --leaf: #6cbf44;
    --lime: #c6de3e;
    --ink: #222222;
    --slate: #4a4a4a;
    --navy: #2b3596;
    --paper: #ffffff;
  }
  * { margin: 0; padding: 0; box-sizing: border-box; }
  html, body { width: 920px; height: 1200px; overflow: hidden; background: var(--paper); }
  .flyer { position: relative; width: 920px; height: 1200px; overflow: hidden; background: var(--paper); font-family: "Open Sans", Arial, sans-serif; }

  .brand-name { position: absolute; left: 40px; top: 62px; font-weight: 700; font-size: 50px; color: var(--sky); letter-spacing: -1px; }
  .tagline { position: absolute; right: 38px; top: 42px; text-align: right; font-style: italic; font-size: 18px; line-height: 22px; color: var(--slate); }

  .headline { position: absolute; left: 0; width: 920px; text-align: center; font-style: italic; font-weight: 700; font-size: 30px; line-height: 38px; color: var(--sky); }
  .headline-threat { top: 160px; }
  .headline-opening { top: 620px; }
  .subline { position: absolute; top: 711px; left: 0; width: 920px; text-align: center; font-style: italic; font-weight: 600; font-size: 20px; color: var(--slate); }

  .photo-band { position: absolute; top: 281px; height: 282px; }
  .photo-pests { left: 0; width: 458px; background: radial-gradient(ellipse at 50% 40%, #dfe9f4 0%, #a9c2dc 60%, #7f9fc2 100%); }
  .photo-intruder { left: 462px; width: 458px; background: radial-gradient(ellipse at 30% 60%, #3b5fa8 0%, #1b2f6e 55%, #0b1436 100%); }
  .band-arc { position: absolute; left: 0; width: 920px; }

  .callout { position: absolute; background: var(--paper); color: var(--sky-deep); font-style: italic; font-size: 13px; line-height: 16px; text-align: center; padding: 7px 8px; box-shadow: 1px 2px 4px rgba(0,0,0,.35); }

  .cloud-panel { position: absolute; left: 0; top: 0; width: 920px; height: 1200px; }
  .offer-title { position: absolute; top: 870px; left: 0; width: 920px; text-align: center; font-family: "Roboto Condensed", "Arial Narrow", sans-serif; font-weight: 700; font-size: 52px; line-height: 58px; color: var(--ink); }
  .offer-promise { position: absolute; top: 1012px; left: 0; width: 920px; text-align: center; font-family: "Roboto Condensed", "Arial Narrow", sans-serif; font-style: italic; font-weight: 700; font-size: 29px; letter-spacing: -0.5px; color: var(--navy); }
  .offer-detail { position: absolute; top: 1050px; left: 0; width: 920px; text-align: center; font-style: italic; font-size: 19px; line-height: 24px; color: var(--slate); }

  .contact { position: absolute; font-style: italic; color: var(--paper); }
  .contact-phone { left: 32px; top: 1140px; font-weight: 700; font-size: 30px; }
  .contact-web { right: 38px; top: 1146px; font-weight: 600; font-size: 21px; }
</style>
</head>
<body>
<main class="flyer">
  <div class="brand-name">BrookVale</div>
  <p class="tagline">Hackers and cyber criminals target small businesses.<br>Proactive support prevents your business from<br>becoming the low hanging fruit criminals love.</p>

  <h1 class="headline headline-threat">210 new malware threats are released every 60 seconds.<br>Their target? Your business.</h1>

  <svg class="band-arc" style="top:244px" width="920" height="40" viewBox="0 244 920 40" aria-hidden="true">
    <path d="M60,281 Q460,236 860,281 Q460,256 60,281 Z" fill="var(--sky)"/>
  </svg>

  <div class="photo-band photo-pests" role="img" aria-label="Photo of dead cockroaches on a pale blue surface, representing malware"></div>
  <div class="photo-band photo-intruder" role="img" aria-label="Photo of a masked burglar at a laptop holding a stolen disc in the dark"></div>

  <svg class="band-arc" style="top:560px" width="920" height="30" viewBox="0 560 920 30" aria-hidden="true">
    <path d="M160,563 Q460,598 760,563 Q460,580 160,563 Z" fill="var(--leaf)"/>
  </svg>

  <p class="callout" style="left:134px;top:291px;width:178px;transform:rotate(-4deg)">This breed disables your antivirus and sends the data to their owners once you're defenceless.</p>
  <p class="callout" style="left:10px;top:447px;width:160px;transform:rotate(8deg)">These two record keystrokes, passwords, and screenshots.</p>
  <p class="callout" style="left:239px;top:478px;width:190px;transform:rotate(-5deg)">They keep coming back, even if you erase everything on your computer.</p>
  <p class="callout" style="left:472px;top:420px;width:185px;transform:rotate(-10deg)">Keylogger software means he now knows all of your usernames and passwords.</p>
  <p class="callout" style="left:708px;top:298px;width:196px;transform:rotate(10deg)">Your company secrets and financial data will give him a nice payday after he's sold them.</p>

  <h2 class="headline headline-opening">Malware gives hackers the opening they need to break<br>into your business.</h2>
  <p class="subline">They take anything and everything once they're inside. If it has value they want it.</p>

  <svg class="cloud-panel" width="920" height="1200" viewBox="0 0 920 1200" aria-hidden="true">
    <defs>
      <radialGradient id="leafGlow" cx="50%" cy="45%" r="60%">
        <stop offset="0" stop-color="var(--lime)"/>
        <stop offset="1" stop-color="var(--leaf)"/>
      </radialGradient>
      <linearGradient id="seaBand" x1="0" x2="1" y1="0" y2="0">
        <stop offset="0" stop-color="var(--sky-deep)"/>
        <stop offset="0.5" stop-color="var(--sky)"/>
        <stop offset="1" stop-color="var(--sky-deep)"/>
      </linearGradient>
    </defs>
    <path d="M0,856 C20,800 220,790 250,832 C270,745 560,745 578,850 C600,795 690,790 720,835 C740,815 800,815 820,868 C840,835 900,835 920,856"
          fill="none" stroke="var(--sky)" stroke-width="9"/>
    <path transform="translate(0,8)" d="M0,856 C20,800 220,790 250,832 C270,745 560,745 578,850 C600,795 690,790 720,835 C740,815 800,815 820,868 C840,835 900,835 920,856 L920,1200 L0,1200 Z"
          fill="url(#leafGlow)"/>
    <path d="M0,1094 Q460,1144 920,1094 L920,1102 Q460,1150 0,1102 Z" fill="var(--leaf)"/>
    <path d="M0,1102 Q460,1150 920,1102 L920,1200 L0,1200 Z" fill="url(#seaBand)"/>
  </svg>

  <h2 class="offer-title">sign up today and<br>get 2 months free it support</h2>
  <p class="offer-promise">We turn your business into a low value target.</p>
  <p class="offer-detail">We make it difficult to access any of your data.<br>There's nothing to steal, even if they're able to break in.</p>

  <p class="contact contact-phone">Call us on 0800 123 4567</p>
  <p class="contact contact-web">www.brookvale-it.co.uk</p>
</main>
</body>
</html>
```